Business card for Luxury Portable Restroom Trailer company

We are a Luxury Portable Restroom Trailer Company Called PELIKAR HIRES. Based in Orange County California. We provide portable restroom trailers for events, such as, Weddings, Concerts, Charity events, Sporting events, Tournaments, Corporate events, ect. We rent and Sell the Luxury restrooms. Our colors are white, grey, and Orange. As you will see in the logo we uploaded.
There are 2 people in the company so the names and titles will change for the 3 people but card will remain the same. Here is the information for each Person: Dennis Moyle CFO 555 018-3647
next Person: Wesley Tanford VP 555 018-3647
Next Person: Miles Tanford CEO 555 018-3647
Information to include on the card: Luxury Restroom Trailers Rental and Sales. Weddings, Concerts, Charity, Sporting and Corp. Events.

```html
<!DOCTYPE html>
<html lang="en">
<head>
<meta charset="utf-8">
<title>PELIKAR HIRES – Business Card</title>
<link href="https://fonts.googleapis.com/css2?family=Open+Sans:wght@400;600;700;800&display=swap" rel="stylesheet">
<style>
  :root{
    --stage:#232323;
    --orange:#f06a22;
    --orange-deep:#e35c17;
    --orange-light:#f4823a;
    --grey:#555658;
    --ink:#1f1f1f;
    --paper:#ffffff;
    --cream:#fdf1e8;
  }
  *{box-sizing:border-box;margin:0;padding:0}
  html,body{width:1200px;height:768px;overflow:hidden;background:var(--stage);font-family:"Open Sans",Arial,sans-serif}
  .canvas{position:relative;width:1200px;height:768px;display:flex;align-items:center;justify-content:center;gap:40px}
  .card{position:relative;width:540px;height:309px;border-radius:22px;overflow:hidden;box-shadow:0 14px 30px rgba(0,0,0,.45)}

  /* front */
  .card--front{background:var(--orange)}
  .front-pattern{position:absolute;inset:0;background:linear-gradient(200deg,var(--orange-light) 0%,var(--orange) 45%,var(--orange-deep) 100%)}
  .wordmark{display:flex;align-items:center;gap:8px;font-weight:800;letter-spacing:.5px;white-space:nowrap}
  .wordmark__square{width:14px;height:14px}
  .card--front .wordmark{position:absolute;right:38px;bottom:70px;color:var(--paper);font-size:24px}
  .card--front .wordmark__square{background:var(--paper)}

  /* back */
  .card--back{background:var(--paper)}
  .back-decor{position:absolute;right:-40px;top:-30px;width:380px;height:300px;border-radius:50%;background:radial-gradient(ellipse at center,var(--cream) 0%,rgba(253,241,232,.6) 55%,rgba(255,255,255,0) 75%)}
  .card--back .wordmark{position:absolute;left:36px;top:132px;color:var(--orange);font-size:23px}
  .card--back .wordmark__square{background:var(--orange)}
  .divider{position:absolute;left:262px;top:62px;width:1px;height:150px;background:var(--ink)}
  .person{position:absolute;left:286px;top:58px}
  .person__name{font-size:26px;font-weight:700;line-height:1.1}
  .person__first{color:var(--orange)}
  .person__last{color:var(--grey)}
  .person__title{font-size:14px;font-weight:600;color:var(--ink);margin:2px 0 10px 18px}
  .contact-list{list-style:none;margin-left:28px}
  .contact-list li{display:flex;align-items:center;gap:8px;font-size:14px;color:var(--ink);line-height:1.5}
  .contact-list svg{width:12px;height:12px;flex:none}
  .services{position:absolute;left:0;right:0;bottom:26px;text-align:center;font-size:14px;color:var(--ink);line-height:1.6}
  .service{display:inline-flex;align-items:center;gap:5px;margin:0 3px}
  .service::before{content:"";width:8px;height:8px;background:var(--orange)}
</style>
</head>
<body>
<main class="canvas">
  <section class="card card--front" aria-label="Card front">
    <div class="front-pattern" role="img" aria-label="Repeating brand-mark pattern on orange"></div>
    <div class="wordmark"><span class="wordmark__square"></span>PELIKAR HIRES</div>
  </section>

  <section class="card card--back" aria-label="Card back">
    <div class="back-decor" role="img" aria-label="Faint large brand mark decoration"></div>
    <div class="wordmark"><span class="wordmark__square"></span>PELIKAR HIRES</div>
    <div class="divider"></div>
    <div class="person">
      <h1 class="person__name"><span class="person__first">Dennis</span> <span class="person__last">Moyle</span></h1>
      <p class="person__title">CFO</p>
      <ul class="contact-list">
        <li><svg viewBox="0 0 12 12"><path d="M2.5 1h2l1 3-1.3 1a6 6 0 0 0 2.8 2.8l1-1.3 3 1v2a1 1 0 0 1-1 1A10 10 0 0 1 1.5 2a1 1 0 0 1 1-1z" fill="#f06a22"/></svg>555 018-3647</li>
        <li><svg viewBox="0 0 12 12"><rect x="1" y="2.5" width="10" height="7" rx="1" fill="#f06a22"/><path d="M1.5 3l4.5 3.5L10.5 3" stroke="#fff" fill="none"/></svg>info@pelikarhires.com</li>
        <li><svg viewBox="0 0 12 12"><circle cx="6" cy="6" r="5" fill="#f06a22"/><path d="M1 6h10M6 1c-2 3-2 7 0 10M6 1c2 3 2 7 0 10" stroke="#fff" stroke-width=".8" fill="none"/></svg>www.pelikarhires.com</li>
      </ul>
    </div>
    <div class="services">
      <div><span class="service">Luxury Restroom Trailers Rental and Sales</span></div>
      <div><span class="service">Weddings</span><span class="service">Concerts</span><span class="service">Charity</span><span class="service">Sporting and Corp</span><span class="service">Events</span></div>
    </div>
  </section>
</main>
</body>
</html>
```